Flyer design

We need a marketing flyer to use when meeting with clients. We may also use it for mailings. Please see the attached document and images. Not all images need to be used. Please feel free to edit / photoshop images. Please also see our website : www.lumivantskinlab.com

Industry/Entity Type

Marketing

```html
<!DOCTYPE html>
<html lang="en">
<head>
<meta charset="utf-8">
<title>Lumivant Dermatology &amp; Dermatopathology – Flyer</title>
<link href="https://fonts.googleapis.com/css2?family=PT+Sans+Narrow:wght@700&family=Source+Sans+3:wght@400;600&display=swap" rel="stylesheet">
<style>
  :root {
    --backdrop: #141414;
    --ink: #222222;
    --paper: #ffffff;
    --red: #ee1c1c;
    --dark: #1c1c1c;
    --strip: #262626;
    --light-text: #f2f2f2;
  }
  * { box-sizing: border-box; margin: 0; padding: 0; }
  html, body { width: 1200px; height: 1000px; overflow: hidden; }
  body {
    background: var(--backdrop);
    font-family: "Source Sans 3", "Helvetica Neue", Arial, sans-serif;
    position: relative;
  }
  .flyer {
    position: absolute; left: 270px; top: 95px;
    width: 640px; height: 800px;
    background: var(--paper);
    overflow: hidden;
  }
  .block { position: absolute; }

  /* Brand */
  .brand { left: 0; top: 0; width: 353px; height: 228px; background: var(--paper);
    display: flex; flex-direction: column; align-items: center; justify-content: center; gap: 14px; }
  .brand-mark { display: flex; align-items: center; gap: 10px; }
  .brand-dot { width: 18px; height: 18px; border-radius: 50%; background: var(--red); }
  .brand-name { font-size: 40px; font-weight: 600; color: var(--ink); letter-spacing: 1px; }
  .brand-sub { text-align: center; font-size: 14px; color: var(--ink); font-weight: 400; line-height: 1.2; }
  .brand-sub .spaced { display: block; color: var(--red); letter-spacing: 9px; font-size: 13px; }

  /* Doctor panel */
  .doctor { left: 353px; top: 0; width: 287px; height: 352px; background: var(--dark); }
  .doctor-photo { position: absolute; left: 0; top: 0; width: 287px; height: 352px;
    background: radial-gradient(ellipse at 55% 30%, #c9c6a0 0%, #6e6b57 35%, #2a2a2a 70%, #1c1c1c 100%); }
  .doctor-name { position: absolute; left: 17px; top: 262px; color: var(--light-text); }
  .doctor-name h1 { font-family: "PT Sans Narrow", "Arial Narrow", sans-serif; font-weight: 700; font-size: 36px; line-height: 1; }
  .doctor-name h1 small { font-family: "Source Sans 3", sans-serif; font-weight: 400; font-size: 14px; margin-left: 4px; }
  .doctor-name p { font-size: 14.5px; line-height: 21px; margin-top: 6px; }

  /* Microscope image */
  .lab-photo { left: 0; top: 228px; width: 353px; height: 249px;
    background: radial-gradient(circle at 38% 80%, #f4eefa 0%, #b596c4 12%, #55505e 35%, #8a8f86 60%, #3a3d38 100%); }
  .tagline { left: 93px; top: 270px; width: 260px; height: 80px; background: var(--red);
    color: var(--paper); font-size: 22px; line-height: 28px; padding: 12px 0 0 14px; }
  .since { left: 150px; top: 362px; width: 190px; text-align: right; color: var(--paper);
    font-size: 17.5px; line-height: 23px; }

  /* Commitment */
  .commitment { left: 353px; top: 352px; width: 287px; height: 125px; background: var(--red);
    color: var(--paper); padding: 24px 14px 0 16px; font-size: 13px; line-height: 17px; }
  .commitment strong { font-size: 17.5px; font-weight: 400; }

  /* Services */
  .services { left: 0; top: 477px; width: 640px; height: 178px; text-align: center; color: var(--ink); padding-top: 6px; }
  .services h2 { font-size: 27px; font-weight: 400; line-height: 32px; }
  .services h3 { font-size: 19px; font-weight: 400; line-height: 24px; }
  .service-list { list-style: none; display: flex; justify-content: center; gap: 12px; font-size: 13px; margin-top: 8px; }
  .service-list li::before { content: ""; display: inline-block; width: 9px; height: 9px; border-radius: 50%;
    background: var(--red); margin-right: 6px; }
  .services p { font-size: 12.5px; line-height: 17px; margin-top: 10px; }
  .services p + p { margin-top: 16px; }

  /* Slide strip */
  .slides { left: 0; top: 655px; width: 640px; height: 105px; background: var(--strip); }
  .slide { position: absolute; top: 8px; height: 90px; border: 1px solid #444; }
  .slide-a { left: 8px; width: 168px; background: radial-gradient(ellipse at 50% 55%, #b28fa0 0%, #c9c08a 40%, #6f6a40 80%, #222 100%); }
  .slide-b { left: 183px; width: 168px; background: radial-gradient(circle, #e3b3c9 0%, #b877a4 50%, #5a4a58 90%); }
  .slide-c { left: 368px; width: 242px; background: linear-gradient(120deg, #f1c4d4 0%, #d67aa7 50%, #b5457f 100%); }

  /* Footer */
  .call { left: 0; top: 760px; width: 288px; height: 40px; background: var(--red); color: var(--paper);
    font-size: 18px; display: flex; align-items: center; padding-left: 32px; }
  .address { left: 288px; top: 760px; width: 352px; height: 40px; background: var(--dark); color: var(--light-text);
    font-size: 12px; display: flex; align-items: center; gap: 10px; padding-left: 12px; }
</style>
</head>
<body>
  <main class="flyer">
    <section class="block brand">
      <div class="brand-mark"><span class="brand-dot"></span><span class="brand-name">Lumivant</span></div>
      <div class="brand-sub"><span class="spaced">LUMIVANT</span>DERMATOLOGY &amp; DERMATOPATHOLOGY</div>
    </section>

    <section class="block doctor">
      <div class="doctor-photo" role="img" aria-label="Portrait of the physician in a dark suit and blue tie"></div>
      <div class="doctor-name">
        <h1>Dana R. Whitfield,<small>M.D.</small></h1>
        <p>Board Certified – Dermatopathology<br>Board Certified – Dermatology</p>
      </div>
    </section>

    <div class="block lab-photo" role="img" aria-label="Close-up of a microscope objective over a lit glass slide"></div>
    <div class="block tagline">The Diagnosis<br>in Focus.</div>
    <div class="block since">Practicing<br>Dermatopathology<br>since 2007.</div>

    <section class="block commitment">
      <strong>Commitment to helping</strong> find solutions, either in-house or through our contacts, for all your dermatopathology needs including but not limited to:
    </section>

    <section class="block services">
      <h2>Dermatopathology consultative service</h2>
      <h3>First or second opinions, off-site or on-site.</h3>
      <ul class="service-list">
        <li>Tissue processing</li>
        <li>Mohs technicians</li>
        <li>Immunohistochemistry and special stains</li>
      </ul>
      <p>Access to an extensive range of special and immunohistochemistry stains, and patient-centered<br>consideration of the judicious use of them.</p>
      <p>Usually 2-3 day turnaround time depending on the circumstance of the case.</p>
    </section>

    <section class="block slides">
      <div class="slide slide-a" role="img" aria-label="Low-power micrograph of a stained skin section"></div>
      <div class="slide slide-b" role="img" aria-label="Micrograph of stained tissue cells"></div>
      <div class="slide slide-c" role="img" aria-label="Pink stained micrograph of skin layers"></div>
    </section>

    <div class="block call">Call Us Now : 800.555.0192</div>
    <div class="block address">
      <svg width="20" height="14" viewBox="0 0 20 14" aria-hidden="true">
        <rect x="0.5" y="0.5" width="19" height="13" fill="none" stroke="#f2f2f2"/>
        <path d="M0.5 0.5 L10 8 L19.5 0.5 M0.5 13.5 L7.5 6 M19.5 13.5 L12.5 6" fill="none" stroke="#f2f2f2"/>
      </svg>
      <span>4120 W. Harbor Ave. #210, Bayview, CA 90000</span>
    </div>
  </main>
</body>
</html>
```